Simple design for eCommerce retailer of Custom Cut Mirror Frames

We need a fresh design for our eCommerce store. Currently, we need a design for each page on the existing site.

Here is the site as it stands right now: glassvela.com

Here is a competitor site that we like. The owner really likes the block look for the home page: framorly.com

Here is a video we would like to feature: https://videohost.example/v/Kp7rTq2LmXa

Here is the color palate, emphasis on the green and purple: https://palettes.example/quiet-bay-theme-48271953/?showPublished=true

Here is an example of a landing page we are currently using: https://glassvela.com/lander-10-off-install/

Font for the site should be the google font Lato

Home page should include the following sections/blocks:

How it works
Shop now
Testimonials
Featured Products
Before and After Gallery
Updates

My team has been slow getting back to me with feedback. I'm pushing them to speed their process up.

Target Market(s)

Women, Ages 35-65+

Number of Pages Required

5+ page

Font styles to use
Sans Serif

Requirements
Must have
• -Before and after gallery
• -Star ratings
• -eCommerce look and feel
• -Info about being able to order free samples
• -Language from the checkmarks on the landing page
• -sleek product page
• -home page should be have a very modern design feel
Should not have
• Product Prices...the user has to use the calculator to determine the price of their purchase.
• Sliders

```html
<!DOCTYPE html>
<html lang="en">
<head>
<meta charset="utf-8">
<title>GlassVela — Custom Mirror Frames</title>
<link href="https://fonts.googleapis.com/css2?family=Lato:wght@400;700;900&display=swap" rel="stylesheet">
<style>
:root{
  --purple:#b27bbd;
  --purple-dark:#9d66a9;
  --teal:#98c2c3;
  --ink:#1d1d1d;
  --grey:#6b6b6b;
  --dark:#3b3b3b;
  --star:#f4c20d;
  --line:#d9d9d9;
}
*{box-sizing:border-box;margin:0;padding:0}
html,body{width:1200px;height:4441px;overflow:hidden}
body{font-family:'Lato',sans-serif;color:var(--ink);background:#fff;position:relative}
.abs{position:absolute}
.btn{display:inline-block;background:var(--purple);color:#fff;font-weight:900;font-size:12px;letter-spacing:.3px;text-transform:uppercase;border-radius:3px;text-align:center}
.accent{color:var(--purple)}
.section-title{font-weight:900;font-size:44px;text-align:center;letter-spacing:-.5px}

.topbar{top:0;left:0;width:1200px;height:45px;background:var(--purple);color:#fff;font-size:12px}
.topbar .item{position:absolute;top:14px;display:flex;align-items:center;gap:8px}
.nav{top:45px;left:0;width:1200px;height:75px;background:#fff;border-bottom:1px solid #eee}
.brand{position:absolute;left:162px;top:22px;display:flex;align-items:center;gap:10px}
.brand-mark{width:26px;height:26px;background:var(--purple)}
.brand-name{font-size:22px;font-weight:700;color:var(--dark)}
.menu{position:absolute;right:162px;top:30px;display:flex;gap:27px;font-size:12.5px;font-weight:700}

.hero{top:120px;left:0;width:1200px;height:600px;background:linear-gradient(100deg,#4a4641 0%,#8c8478 35%,#cfc3ad 65%,#b79a72 100%)}
.hero h1{position:absolute;left:162px;top:150px;color:#fff;font-size:58px;font-weight:900;line-height:1.05;text-transform:uppercase}
.hero p{position:absolute;left:162px;top:290px;color:#fff;font-size:22px}
.hero .btn{position:absolute;left:162px;top:340px;width:188px;height:52px;line-height:52px;font-size:14px}
.hero-slope{position:absolute;left:0;bottom:0;width:1200px;height:60px}

.how{top:720px;left:0;width:1200px;height:404px}
.how .section-title{margin-top:28px}
.steps{position:absolute;top:140px;left:0;width:1200px;height:260px}
.step{position:absolute;width:180px;text-align:center;font-size:13px;font-weight:700;line-height:1.5}
.step .circle{width:116px;height:116px;margin:0 auto 26px;border-radius:50%;background:var(--purple);box-shadow:0 0 0 7px #dcc3e1;display:flex;align-items:center;justify-content:center}

.products{top:1124px;left:0;width:1200px;height:614px;background:linear-gradient(180deg,#2f2f2f,#474747 70%,#3b3d35)}
.products .section-title{color:#fff;margin-top:46px}
.card{position:absolute;background:#fff;text-align:center}
.card .pic{width:100%;background:linear-gradient(135deg,#5a3a22 0 18%,#b9d9da 18%,#a8cfd0)}
.card h3{font-size:13px;font-weight:700;margin-top:16px}
.card .sub{font-size:11px;color:#a9c7c8;margin-top:6px}
.stars{color:var(--star);font-size:14px;letter-spacing:4px;margin-top:8px}
.card .btn{width:98px;height:34px;line-height:34px;font-size:11px;margin-top:12px}
.view-all{position:absolute;left:550px;top:530px;width:100px;height:36px;line-height:36px;font-size:11px}

.band{top:1738px;left:0;width:1200px;height:115px;background:var(--purple);color:#fff}
.band h2{position:absolute;left:162px;top:38px;font-size:32px;font-weight:900}
.band .outline{position:absolute;left:800px;top:40px;width:130px;height:36px;line-height:36px;background:#fff;color:var(--purple);font-weight:900;font-size:13px;text-align:center;border-radius:2px}

.gallery{top:1853px;left:0;width:1200px;height:411px}
.g-before{left:0;top:0;width:476px;height:411px;background:linear-gradient(180deg,#cfcfcf 0%,#8d8d8d 55%,#e9e0da 72%,#2e2f31 78%)}
.g-after{left:724px;top:0;width:476px;height:411px;background:linear-gradient(180deg,#2b2a2a 0%,#a5a5a5 20%,#7f7f7f 55%,#e9e0da 72%,#2e2f31 78%)}
.g-center{left:476px;top:0;width:248px;height:411px;background:var(--teal);color:#fff;text-align:center}
.g-center h2{font-size:28px;font-weight:700;margin-top:52px;line-height:1.25}
.g-center p{font-size:11px;line-height:1.75;padding:0 22px;margin-top:20px}
.g-center .wbtn{display:inline-block;margin-top:26px;width:112px;height:36px;line-height:36px;background:#fff;color:var(--ink);font-weight:900;font-size:12px}
.tag{position:absolute;top:320px;background:#fff;font-weight:900;font-size:15px;padding:0 24px;height:44px;line-height:44px}

.featured{top:2264px;left:0;width:1200px;height:550px}
.featured .section-title{margin-top:60px}
.fcard{position:absolute;top:160px;width:204px;height:317px;background:#fff;text-align:center;box-shadow:0 0 0 1px #e5e5e5,0 4px 8px rgba(0,0,0,.08)}
.fcard .pic{height:164px}
.fcard h3{font-size:13px;font-weight:700;margin-top:20px}
.fcard .sub{font-size:11px;color:#a9c7c8;margin-top:6px}
.fcard .btn{width:98px;height:32px;line-height:32px;font-size:11px;margin-top:12px}

.guarantee{top:2814px;left:0;width:1200px;height:338px}
.guarantee h2{position:absolute;left:162px;top:66px;font-size:38px;font-weight:900;line-height:1.15}
.guarantee p{position:absolute;left:162px;top:172px;font-size:16px;color:var(--grey);line-height:1.6;font-family:Arial,sans-serif}
.guarantee .btn{position:absolute;left:162px;top:240px;width:112px;height:36px;line-height:36px;font-size:11px}
.video{position:absolute;left:586px;top:0;width:614px;height:338px;background:linear-gradient(120deg,#1a1b22,#2e2b3b 45%,#403846 70%,#6b6462)}
.play{position:absolute;left:270px;top:132px;width:74px;height:74px;border-radius:50%;background:#fff;display:flex;align-items:center;justify-content:center}

.promo{top:3152px;left:0;width:1200px;height:112px;background:var(--purple);color:#fff;text-align:center;font-size:25px;font-weight:700;line-height:112px}

.testimonials{top:3264px;left:0;width:1200px;height:374px;background:linear-gradient(180deg,#1b1b1b,#2d2b29 60%,#1e1e1e)}
.testimonials .section-title{color:#fff;margin-top:44px}
.tcard{position:absolute;top:144px;width:276px;height:149px;background:#fff;border-radius:4px;padding:14px 16px;font-size:11px;color:var(--grey);line-height:1.75}
.tcard .who{color:var(--purple);font-weight:700;font-size:11px}
.tcard .stars{margin:2px 0 6px;font-size:13px}

.news{top:3638px;left:0;width:1200px;height:542px}
.news .section-title{margin-top:50px}
.news .lead{width:520px;margin:14px auto 0;font-size:11.5px;color:var(--grey);text-align:center;line-height:1.75}
.news .field{position:absolute;left:310px;top:172px;width:414px;height:42px;background:#efefef;border:1px solid #ddd;font-size:12px;font-weight:700;padding-left:16px;line-height:40px}
.news .btn{position:absolute;left:738px;top:172px;width:150px;height:42px;line-height:42px;font-size:13px}

.footer{top:4180px;left:0;width:1200px;height:261px;background:#050505}
.socials{position:absolute;top:156px;left:514px;display:flex;gap:12px}
.socials span{width:34px;height:34px;border-radius:50%}
.socials .s1{background:var(--purple)}
.socials .s2,.socials .s3,.socials .s4{border:2px solid #fff}
.copy{position:absolute;top:222px;width:1200px;text-align:center;color:#fff;font-size:11px}

.contact{top:3922px;left:186px;width:828px;height:376px;box-shadow:0 2px 10px rgba(0,0,0,.15);display:flex}
.contact .form{width:452px;background:#fff;padding:36px 26px}
.contact .info{flex:1;background:var(--purple);color:#fff;padding:36px 34px}
.contact h2{font-size:30px;font-weight:900}
.contact .info h2{font-weight:700}
.field-line{font-size:11px;border-bottom:1px solid var(--line);padding:18px 0 8px;width:376px}
.field-line.tall{height:82px}
.contact .btn{margin-top:22px;width:142px;height:36px;line-height:36px;font-size:12px}
.info-row{display:flex;align-items:center;gap:14px;font-size:12px;margin-top:18px;line-height:1.4}
.info-row .ic{width:36px;height:36px;border-radius:50%;background:#fff;display:flex;align-items:center;justify-content:center;flex:none}
.map-btn{display:inline-block;margin-top:32px;border:1.5px solid #fff;width:158px;height:38px;line-height:36px;text-align:center;font-weight:900;font-size:12px}
</style>
</head>
<body>

<header class="topbar abs">
  <span class="item" style="left:160px"><span style="width:22px;height:15px;background:#2b3f8f;display:inline-block;border-radius:2px"></span></span>
  <span class="item" style="left:204px">
    <svg width="14" height="14" viewBox="0 0 24 24" fill="none" stroke="#fff" stroke-width="2"><path d="M5 3h4l2 5-3 2a12 12 0 0 0 6 6l2-3 5 2v4a2 2 0 0 1-2 2A17 17 0 0 1 3 5a2 2 0 0 1 2-2z"/></svg>
    +1-(555) 014-3870</span>
  <span class="item" style="left:386px">
    <svg width="16" height="12" viewBox="0 0 24 18" fill="none" stroke="#fff" stroke-width="2"><rect x="1" y="1" width="22" height="16"/><path d="M1 1l11 9 11-9"/></svg>
    support@glassvela.com</span>
  <span class="item" style="left:986px">
    <svg width="14" height="16" viewBox="0 0 14 16" fill="#fff"><circle cx="7" cy="4" r="4"/><path d="M0 16c0-5 3-7 7-7s7 2 7 7z"/></svg>
  </span>
  <span class="item" style="left:1024px">
    <svg width="14" height="16" viewBox="0 0 14 16" fill="#fff"><path d="M1 5h12l-1 11H2z"/><path d="M4 5a3 3 0 0 1 6 0" stroke="#fff" fill="none" stroke-width="1.5"/></svg>
  </span>
</header>

<nav class="nav abs">
  <div class="brand"><span class="brand-mark"></span><span class="brand-name">GlassVela</span></div>
  <div class="menu"><span>Home</span><span>How Its Works</span><span>Shop Now</span><span>Featured Products</span><span>Gallery</span><span>Testimonials</span></div>
</nav>

<section class="hero abs" role="img" aria-label="Bathroom with an arched mirror set in a custom cut frame against a stone wall">
  <h1>Frame any mirror<br>in your house</h1>
  <p>With an elegant custom cut frame</p>
  <span class="btn">Get a free sample</span>
  <svg class="hero-slope" viewBox="0 0 1200 60" preserveAspectRatio="none"><path d="M0 60L1200 24V60Z" fill="#fff"/></svg>
</section>

<section class="how abs">
  <h2 class="section-title">How Its <span class="accent">Work</span></h2>
  <div class="steps">
    <svg class="abs" style="left:0;top:0" width="1200" height="120" fill="none" stroke="#b9b9b9" stroke-width="1.5" stroke-dasharray="3 4">
      <path d="M327 30C370 0 420 0 440 20"/>
      <path d="M540 90C580 120 640 120 660 90"/>
      <path d="M755 30C790 -5 850 0 870 25"/>
    </svg>
    <div class="step" style="left:178px;top:0"><div class="circle">
      <svg width="56" height="56" viewBox="0 0 56 56" fill="none" stroke="#fff" stroke-width="3"><rect x="6" y="8" width="30" height="8"/><rect x="6" y="22" width="30" height="8"/><rect x="6" y="36" width="30" height="8"/><path d="M30 48l18-18M40 26l8 8"/></svg>
    </div>Assembly &amp;<br>Installation</div>
    <div class="step" style="left:388px;top:0"><div class="circle">
      <svg width="56" height="56" viewBox="0 0 56 56" fill="none" stroke="#fff" stroke-width="3"><path d="M32 8l16 16-10 6-12-12z"/><path d="M27 20L10 40a4 4 0 0 0 6 6l20-17"/></svg>
    </div>How to paint your<br>Frames</div>
    <div class="step" style="left:606px;top:0"><div class="circle">
      <svg width="56" height="56" viewBox="0 0 56 56" fill="#fff"><path d="M8 16l16 12-16 12z"/><path d="M48 16L32 28l16 12z"/><rect x="26" y="8" width="4" height="40"/></svg>
    </div>Why frame your<br>Bathroom Mirrors?</div>
    <div class="step" style="left:830px;top:0"><div class="circle">
      <svg width="56" height="56" viewBox="0 0 56 56" fill="none" stroke="#fff" stroke-width="3"><ellipse cx="28" cy="20" rx="12" ry="14"/><path d="M14 40h28M20 40v10M36 40v10M28 34v6"/></svg>
    </div>Large or Unique<br>Mirrors</div>
  </div>
</section>

<section class="products abs">
  <h2 class="section-title">Our <span class="accent">Products</span></h2>
  <div class="card" style="left:162px;top:145px;width:276px;height:336px">
    <div class="pic" style="height:188px" role="img" aria-label="Corner of a wood-tone frame sample"></div>
    <h3>Harbor Mocha</h3><div class="sub">Modern Look</div><div class="stars">★★★★★</div><span class="btn">Shop now</span>
  </div>
  <div class="card" style="left:462px;top:145px;width:276px;height:336px">
    <div class="pic" style="height:188px;background:linear-gradient(135deg,#1f1f1f 0 18%,#b9d9da 18%,#a8cfd0)" role="img" aria-label="Corner of a dark ornate frame sample"></div>
    <h3>Siena Bronze</h3><div class="sub">Olde World Look</div><div class="stars">★★★★★</div><span class="btn">Shop now</span>
  </div>
  <div class="card" style="left:762px;top:145px;width:276px;height:336px">
    <div class="pic" style="height:188px;background:linear-gradient(135deg,#d8d0c0 0 18%,#b9d9da 18%,#a8cfd0)" role="img" aria-label="Corner of a distressed white frame sample"></div>
    <h3>Verona Distressed White</h3><div class="sub">Verona Fashion Look</div><div class="stars">★★★★★</div><span class="btn">Shop now</span>
  </div>
  <span class="btn view-all">View all</span>
</section>

<section class="band abs">
  <h2>Quick, Easy, and Affordable Frames</h2>
  <span class="outline">SHOP NOW</span>
</section>

<section class="gallery abs">
  <div class="g-before abs" role="img" aria-label="Bathroom vanity with an unframed mirror, before">
    <span class="tag" style="left:0">BEFORE</span>
  </div>
  <div class="g-center abs">
    <h2>View Our<br>Gallery</h2>
    <p>With residential construction costs rising, contractors and homeowners often choose to install sheet glass mirrors in bathrooms and living spaces. While this is functional and economical.</p>
    <span class="wbtn">VIEW ALL</span>
  </div>
  <div class="g-after abs" role="img" aria-label="Same bathroom vanity with the mirror in a black frame, after">
    <span class="tag" style="left:0">AFTER</span>
  </div>
</section>

<section class="featured abs">
  <h2 class="section-title">Featured <span class="accent">Products</span></h2>
  <div class="fcard" style="left:162px">
    <div class="pic" style="background:linear-gradient(135deg,#7d766a 0 22%,#c3dcdd 22%,#b3d3d4)" role="img" aria-label="Silver frame sample corner"></div>
    <h3>Lumen Silver</h3><div class="sub">Modern Look</div><div class="stars">★★★★★</div><span class="btn">Shop now</span>
  </div>
  <div class="fcard" style="left:386px">
    <div class="pic" style="background:linear-gradient(135deg,#2a2622 0 22%,#c3dcdd 22%,#b3d3d4)" role="img" aria-label="Bronze frame sample corner"></div>
    <h3>Coastline Bronze</h3><div class="sub">Elegant Look</div><div class="stars">★★★★★</div><span class="btn">Shop now</span>
  </div>
  <div class="fcard" style="left:610px">
    <div class="pic" style="background:linear-gradient(135deg,#5b3a28 0 22%,#c3dcdd 22%,#b3d3d4)" role="img" aria-label="Black and silver frame sample corner"></div>
    <h3>Coastline Black Silver</h3><div class="sub">Versatile Look</div><div class="stars">★★★★★</div><span class="btn">Shop now</span>
  </div>
  <div class="fcard" style="left:834px">
    <div class="pic" style="background:linear-gradient(135deg,#2e2724 0 22%,#c3dcdd 22%,#b3d3d4)" role="img" aria-label="Espresso frame sample corner"></div>
    <h3>Harbor Espresso</h3><div class="sub">Modern Look</div><div class="stars">★★★★★</div><span class="btn">Shop now</span>
  </div>
</section>

<section class="guarantee abs">
  <h2>100% SATISFACTION<br>GUARANTEE!</h2>
  <p>Unsure? – Don't Worry, We Will Walk You Through<br>Every Step Of The Process.</p>
  <span class="btn">Shop now</span>
  <div class="video" role="img" aria-label="Video still of a frame being fitted onto a bathroom mirror">
    <span class="play"><svg width="26" height="28" viewBox="0 0 26 28"><path d="M2 1l23 13L2 27z" fill="var(--purple)"/></svg></span>
  </div>
</section>

<section class="promo abs">Get up to 7 Samples FREE! Use code: freesample At Checkout.</section>

<section class="testimonials abs">
  <h2 class="section-title">Our <span class="accent">Testimonials</span></h2>
  <div class="tcard" style="left:162px"><div class="who">Dana R., Seabright, Ca</div><div class="stars">★★★★★</div>" Great product and great service! Adding frames to our mirrors made all the difference in how the master bath looks. You can't beat GlassVela for the money! "</div>
  <div class="tcard" style="left:462px"><div class="who">Marla T., Oakvale, Ca</div><div class="stars">★★★★★</div>" We were so happy with the first two frames we purchased; we purchased a frame for our other bathroom. I would highly recommend this company. "</div>
  <div class="tcard" style="left:762px"><div class="who">Joan P., Millbrook, Ca</div><div class="stars">★★★★★</div>" I did my three bathrooms and couldn't be happier, what a difference the new frames made! Do yourself a favor and frame your mirrors, you'll be happy you did. "</div>
</section>

<section class="news abs">
  <h2 class="section-title">Sign Up To <span class="accent">Our Newsletter</span></h2>
  <p class="lead">Lorem Ipsum is simply dummy text of the printing and typesetting industry. Lorem Ipsum has been the industry's standard dummy text ever since the 1500s</p>
  <div class="field">Email:</div>
  <span class="btn">Subscribe now !</span>
</section>

<footer class="footer abs">
  <div class="socials"><span class="s1"></span><span class="s2"></span><span class="s3"></span><span class="s4"></span></div>
  <div class="copy">Copyright © 2019. <span class="accent">GlassVela</span>, All Right Reserved. | Terms &amp; Conditions</div>
</footer>

<section class="contact abs">
  <div class="form">
    <h2>Contact <span class="accent">Us</span></h2>
    <div class="field-line" style="margin-top:8px">Name:</div>
    <div class="field-line">Email:</div>
    <div class="field-line">Phone No:</div>
    <div class="field-line tall">Messages:</div>
    <span class="btn">Send message</span>
  </div>
  <div class="info">
    <h2>Our Info</h2>
    <div class="info-row" style="margin-top:40px"><span class="ic"><svg width="16" height="16" viewBox="0 0 24 24" fill="none" stroke="var(--purple)" stroke-width="2.4"><path d="M5 3h4l2 5-3 2a12 12 0 0 0 6 6l2-3 5 2v4a2 2 0 0 1-2 2A17 17 0 0 1 3 5a2 2 0 0 1 2-2z"/></svg></span>+1-(555) 014-3870</div>
    <div class="info-row"><span class="ic"><svg width="16" height="12" viewBox="0 0 24 18" fill="none" stroke="var(--purple)" stroke-width="2.4"><rect x="1" y="1" width="22" height="16"/><path d="M1 1l11 9 11-9"/></svg></span>support@glassvela.com</div>
    <div class="info-row"><span class="ic"><svg width="14" height="18" viewBox="0 0 14 20" fill="var(--purple)"><path d="M7 0a7 7 0 0 1 7 7c0 5-7 13-7 13S0 12 0 7a7 7 0 0 1 7-7z"/><circle cx="7" cy="7" r="2.5" fill="#fff"/></svg></span>82 Lantern Park Rd, Unit 4,<br>Brookhaven, CA 90210</div>
    <span class="map-btn">VIEW ONLINE MAP</span>
  </div>
</section>

</body>
</html>
```